Coaching Workbook (for life & health coaching industry)

I created a coaching workbook using Canva. I would like it recreated more professionally in PowerPoint with better images and creative design using my 3 branding colors (teal primary, salmon secondary, and turquoise splash here and there).

Please use the attached image of lady sitting on dock at the lake on the first slide for the cover along with my logo and my titles (similar to my Canva version on my website).

My version of the workbook is attached. Thank you for turning my drab into fab:-) Merle Quistad, Life & Health Coach, Grief Recovery Specialist
Updates

To ensure clarity, I am looking for a PowerPoint (prefer vertical format) for a coaching manual FROM the material in the version that I created in Canva, which is currently on my website as a download at the bottom of my coaching page: https://brightmeadowguide.example/coaching-2 I will upload the pdf file as well as the example that I'm trying to recreate in PowerPoint, but more professionally and creatively. Thank You! Merle Quistad

Target Market(s)

My target audience is primarily female, with a few males each year, ages range from mid-twenties to sixties. Everyone will experience the pain of loss and grief. Women are more prone to reach out for help sooner.

Industry/Entity Type

Life Coaching

Font styles to use
Serif

Requirements
Must have
• Want it to feel personal, not corporate if that makes sense.
• Must use my 3 branding colors: HEX # 2994ae, 10dfd3, fa8070.
• Please use Playfair Display font for consistency with my website.
• The text for the workbook is included in the Word document attached below.
Should not have
• I'm not looking for the material on my website to be the focus of this workbook. I want the Canva version that I created to be converted more professionally and creatively in PowerPoint, so I can manage moving forward.

```html
<!DOCTYPE html>
<html lang="en">
<head>
<meta charset="UTF-8">
<title>Smart Goals – Coaching Workbook Page</title>
<link rel="stylesheet" href="https://fonts.googleapis.com/css2?family=Playfair+Display:wght@700;900&family=Poppins:wght@500&family=Montserrat:wght@400&display=swap">
<style>
  :root {
    --backdrop: #3a3b3d;
    --page: #ffffff;
    --salmon: #fa8070;
    --teal: #2994ae;
    --turquoise: #10dfd3;
    --link: #2ba3d6;
    --ink: #3b3b3b;
    --ink-soft: #555555;
  }
  * { margin: 0; padding: 0; box-sizing: border-box; }
  html, body {
    width: 1200px; height: 1200px; overflow: hidden;
    background: var(--backdrop);
  }
  .page {
    position: absolute; left: 175px; top: 40px;
    width: 851px; height: 1118px;
    background: var(--page);
  }
  .page-header {
    position: absolute; left: 0; top: 0;
    width: 100%; height: 81px;
    background: var(--salmon);
  }
  .page-title {
    position: absolute; left: 25px; top: 6px;
    font-family: "Playfair Display", serif;
    font-weight: 900; font-size: 56px; line-height: 1.2;
    color: #fff;
  }
  .photo { position: absolute; }
  .photo--meal {
    left: 0; top: 81px; width: 409px; height: 589px;
    background: linear-gradient(160deg, #7fb0c4 0%, #c9a46a 40%, #8a5a34 70%, #3d2b22 100%);
  }
  .photo--fitness {
    left: 409px; top: 81px; width: 442px; height: 294px;
    background: linear-gradient(180deg, #eef0f0 0%, #5aa3c0 45%, #3b8fb0 65%, #d9b08a 100%);
  }
  .photo--hands {
    left: 409px; top: 375px; width: 442px; height: 295px;
    background: linear-gradient(180deg, #b8c4c6 0%, #a9b8b4 50%, #d8c1b0 100%);
  }
  .info-card {
    position: absolute; left: 35px; top: 622px;
    width: 781px; height: 448px;
    background: var(--page);
    box-shadow: 0 3px 5px rgba(0,0,0,0.35);
  }
  .intro {
    position: absolute; left: 12px; top: 32px; width: 750px;
    font-family: "Poppins", sans-serif; font-weight: 500;
    font-size: 15px; line-height: 23px; color: var(--ink);
  }
  .intro .accent { color: var(--salmon); }
  .smart-list { list-style: none; }
  .smart-item {
    position: absolute; left: 76px;
    font-family: "Montserrat", sans-serif; font-size: 16px;
    color: var(--ink-soft); white-space: nowrap;
  }
  .smart-item .term {
    font-family: "Playfair Display", serif; font-weight: 700;
    font-size: 22px; color: var(--salmon);
  }
  .smart-item--s { top: 116px; }
  .smart-item--m { top: 165px; }
  .smart-item--a { top: 215px; }
  .smart-item--r { top: 265px; }
  .smart-item--t { top: 313px; }
  .worksheet-note {
    position: absolute; left: 12px; top: 380px;
    font-family: "Montserrat", sans-serif; font-size: 16px;
    color: var(--ink-soft);
  }
  .worksheet-note a { color: var(--link); text-decoration: underline; }
</style>
</head>
<body>
  <main class="page">
    <header class="page-header">
      <h1 class="page-title">Smart Goals</h1>
    </header>

    <div class="photo photo--meal" role="img" aria-label="Photo of a burger with fries and a drink on a wooden table"></div>
    <div class="photo photo--fitness" role="img" aria-label="Photo of hand weights, an exercise ball and running shoes"></div>
    <div class="photo photo--hands" role="img" aria-label="Photo of two hands linked by the little fingers"></div>

    <section class="info-card">
      <p class="intro"><span class="accent">SMART</span> goal setting is a coaching methodology that provides structure to the process of formulating, planning, and achieving your goals. The acronym stands for:</p>
      <ul class="smart-list">
        <li class="smart-item smart-item--s"><span class="term">SPECIFIC</span> - What exactly do you want to accomplish?</li>
        <li class="smart-item smart-item--m"><span class="term">Measurable</span> - How will you track your progress to stay motivated?</li>
        <li class="smart-item smart-item--a"><span class="term">Achievable</span> - How will you accomplish this goal?</li>
        <li class="smart-item smart-item--r"><span class="term">Relevant</span> - Is this goal realistic given everything else on your plate?</li>
        <li class="smart-item smart-item--t"><span class="term">Timely</span> - What is the target date for completion?</li>
      </ul>
      <p class="worksheet-note"><a href="#">This SMART Goal worksheet</a> can help you make changes to any area of your life.</p>
    </section>
  </main>
</body>
</html>
```